SEO optimized website for Nu-Crest Corporate identity

I need an eye catching website (Flash splash is OK-I think) to help me promote my company of 10 years: Nu-Crest Inc. - we recently just awarded a design win for my logo design. See attached files.

The company name is Nu-Crest Inc. My current website is www.nu-crest.ca and we specialize in large infrastructure - technology integration, both management and engineering. We have worked almost exclusively on KORB projects and wish to promote that.

I need it to be flexible enough for me to add pages for existing case studies and future case studies.

It is difficult to marry technology and green but do your best as I would like to highlight our KORB AP staff members.

The other side of my business is Small Medium Sized Business support and engineering. VOIP, Server, Desktop we have done it all.

My current site is www.nu-crest.ca
Updates

Please use newly attached logo for designs.

All Please see some sample images to incorporate into the deisgns

Reason: Need more time to evaluate

Please use the correct/new logo in all designs

Please use the updated l;og that was included. Thank you.

Reason: I would like designers to modify their deisgns with the actual company logo. Only one design er has gotten it right. Please modify.

Reason: Still no time to devote to this. Sorry

Reason: Not ready to focus on it

Please only use the logo supplied int he source file zip

Target Market(s)

Both large infrstructure facility owners and small and medium sized businesses.

Industry/Entity Type

Business

Requirements
Must have
• SEO optimization
Easy for me to provide content going forward
Link to my FTP site
Links to my main partners
Separate login are for my clients to store files

```html
<!DOCTYPE html>
<html lang="en">
<head>
<meta charset="utf-8">
<title>Nu-Crest — Technology Infrastructure Engineering</title>
<link rel="stylesheet" href="https://fonts.googleapis.com/css2?family=Arimo:wght@400;700&display=swap">
<style>
  :root {
    --orange: #ff6a00;
    --navy: #1d3450;
    --ink: #222;
    --white: #fff;
    --panel-top: #d9dde0;
    --panel-bottom: #f4f5f6;
    --hero-dark: #0a0c12;
    --hero-mid: #2a2630;
  }
  * { box-sizing: border-box; margin: 0; padding: 0; }
  html, body { width: 1200px; height: 942px; overflow: hidden; background: var(--white); }
  body { position: relative; font-family: "Arimo", Arial, sans-serif; color: var(--ink); }

  .site-header {
    position: absolute; left: 0; top: 0; width: 1200px; height: 106px;
    background: linear-gradient(#ffffff 0%, #f1f1f1 60%, #e2e2e2 100%);
    border-bottom: 1px solid #9aa;
  }
  .brand { position: absolute; left: 36px; top: 30px; display: flex; align-items: center; gap: 12px; }
  .brand-mark { width: 34px; height: 34px; border-radius: 50%; background: var(--orange); }
  .brand-name { font-size: 44px; font-weight: 400; color: var(--navy); line-height: 1; letter-spacing: -1px; }

  .main-nav { position: absolute; top: 64px; left: 481px; display: flex; }
  .main-nav a {
    display: block; height: 35px; padding: 14px 0 0 12px;
    border-left: 5px solid var(--orange); color: #1a1a1a; text-decoration: none; font-size: 17px;
  }
  .main-nav a:nth-child(1) { width: 102px; }
  .main-nav a:nth-child(2) { width: 126px; }
  .main-nav a:nth-child(3) { width: 120px; }
  .main-nav a:nth-child(4) { width: 120px; }
  .main-nav a:nth-child(5) { width: 116px; }

  .hero {
    position: absolute; left: 0; top: 107px; width: 1200px; height: 607px;
    background:
      radial-gradient(ellipse 420px 140px at 600px 470px, rgba(200,190,150,.55), transparent 70%),
      radial-gradient(ellipse 300px 260px at 330px 330px, rgba(120,110,100,.45), transparent 70%),
      linear-gradient(180deg, var(--hero-dark) 0%, #15151c 40%, var(--hero-mid) 70%, #4a3f32 85%, #2a241e 100%);
  }
  .search { position: absolute; right: 62px; top: 29px; display: flex; align-items: center; gap: 6px; }
  .search input {
    width: 192px; height: 27px; border: 1px solid #ccc; border-radius: 4px; padding: 0 12px;
    font: 14px "Arimo", Arial, sans-serif; color: #333; background: #fff;
  }
  .go {
    display: inline-flex; align-items: center; justify-content: center;
    width: 28px; height: 28px; border-radius: 50%; background: var(--orange);
    color: #fff; font-size: 11px; font-weight: 700; border: 2px solid #fff3;
  }
  .hero-copy { position: absolute; left: 547px; top: 86px; width: 525px; color: var(--white); }
  .hero-copy h1 { color: var(--orange); font-size: 24px; font-weight: 700; margin-bottom: 14px; }
  .hero-copy h1 strong { font-size: 31px; }
  .hero-copy p { font-size: 14.4px; line-height: 22px; text-align: justify; margin-bottom: 20px; }
  .read-more-btn {
    position: absolute; left: 546px; top: 263px; width: 140px; height: 35px; border-radius: 5px;
    background: var(--orange); color: #fff; font-size: 18px; font-weight: 700;
    display: flex; align-items: center; text-decoration: none;
  }
  .read-more-btn span:first-child { padding: 0 8px 0 10px; border-right: 1px solid #fff8; }
  .read-more-btn span:last-child { padding-left: 6px; }
  .slide-thumbs { position: absolute; left: 894px; top: 263px; display: flex; gap: 11px; }
  .slide-thumbs span { width: 37px; height: 37px; border: 3px solid #fff; border-radius: 5px; background: linear-gradient(#243050, #8a6a3a); }

  .feature-row { position: absolute; left: 0; top: 715px; width: 1200px; height: 182px; display: flex; }
  .feature-bar { width: 13px; background: var(--orange); }
  .feature { flex: 1; position: relative; background: linear-gradient(var(--panel-top), var(--panel-bottom)); padding: 12px 34px 0 36px; }
  .feature h2 { color: var(--orange); font-size: 24px; font-weight: 700; margin-bottom: 10px; }
  .feature p { font-size: 15px; line-height: 24px; color: var(--ink); text-align: justify; }
  .feature ul { list-style: none; font-size: 15px; line-height: 24px; }
  .feature li::before { content: "›"; font-weight: 700; font-size: 20px; margin-right: 8px; color: #111; }
  .feature-more { position: absolute; right: 34px; bottom: 22px; display: flex; align-items: center; gap: 14px; font-size: 17px; color: var(--navy); }
  .feature-more .go { width: 32px; height: 32px; background: var(--navy); color: var(--orange); border: none; box-shadow: 0 3px 3px #0003; }

  .site-footer { position: absolute; left: 0; top: 897px; width: 1200px; height: 45px; padding: 16px 18px 0; display: flex; justify-content: space-between; font-size: 13px; color: #111; }
  .site-footer nav a { color: #111; text-decoration: none; }
</style>
</head>
<body>
  <header class="site-header">
    <div class="brand"><span class="brand-mark"></span><span class="brand-name">Nu-Crest</span></div>
    <nav class="main-nav">
      <a href="#">Home</a><a href="#">About Us</a><a href="#">Services</a><a href="#">Partners</a><a href="#">Careers</a><a href="#">Contact Us</a>
    </nav>
  </header>

  <section class="hero" role="img" aria-label="Night city skyline with illuminated towers and a glass building under construction">
    <form class="search"><input type="text" value="Search..." aria-label="Search"><span class="go">GO</span></form>
    <div class="hero-copy">
      <h1>A borad range of <strong>Technology Expertise</strong></h1>
      <p>With over 100 years of collective technology and operations experience under ourbelt, the Nu-Crest team can deliver you into the future.</p>
      <p>We provide Professional Servicesin:Project Management. Technical Engineering and Srvice &amp; Support for same of Canads's best and largest companies.</p>
    </div>
    <a class="read-more-btn" href="#"><span>Read More</span><span>&gt;&gt;</span></a>
    <div class="slide-thumbs"><span></span><span></span><span></span><span></span></div>
  </section>

  <section class="feature-row">
    <div class="feature-bar"></div>
    <article class="feature">
      <h2>Core Capabilities</h2>
      <p>Nu-Crest is a leader in Technology Infrastructure Engineering and Project Management...</p>
      <div class="feature-more">Read More <span class="go">GO</span></div>
    </article>
    <div class="feature-bar"></div>
    <article class="feature">
      <h2>Corporate Links</h2>
      <ul><li>Nu-Crest FTP Site</li><li>Web Timesheets</li><li>Nu-Crest for Clients</li><li>Job Site Photos</li></ul>
      <div class="feature-more">Read More <span class="go">GO</span></div>
    </article>
    <div class="feature-bar"></div>
    <article class="feature">
      <h2>Our Main Services</h2>
      <p>A borad range of technology expertise, including but not limited to:</p>
      <ul><li>IT Project Management</li><li>VIOP Implementations</li><li>Virtualization</li></ul>
      <div class="feature-more">Read More <span class="go">GO</span></div>
    </article>
  </section>

  <footer class="site-footer">
    <nav><a href="#">Sitemap</a> &nbsp;| &nbsp;<a href="#">Legal</a> &nbsp;| &nbsp;<a href="#">Privacy Policy</a> &nbsp;| &nbsp;<a href="#">Contact Us</a></nav>
    <span>© 2011 Nu-Crest. All rights reserved.</span>
  </footer>
</body>
</html>
```